Small environmental consultancy needs a simple but professional web design

We are a boutique environmental consultancyand contracting business located in Margaret River in the South West of Western Australia.

We have two arms
1) Consulting which offers environmental planning, management and assessment services primarily to local government and the development industry.
2) Contracting which implements on site plans and on ground works primarily involving revegetation, bush regeneration and environmental weed control.

We need a simple yet professional web design within the wordpress platform that commmunicates professionalism, experience and technical expertise without appearing too corporate.

Something like this structure appeals:
http://tarnwick.net.au/environment-services/
or
http://www.brackleyfieldworks.com.au/index.php

(without the image gallery function)

Target Market(s)

Local Government Officers deciding on tenders;
Developers, Engineers, Town Planning consultants looking for environmental expertise

Industry/Entity Type

Business

Number of Pages Required

5+ page

Font styles to use
Sans Serif

Colors
33a6d7
9bcb3c

Requirements
Must have
• Pages required include:
• Home
• Environmental Planning and Management
• Revegetation and Regeneration Implementation (This page can mirror the Environmental Planning and Management page exactly in structure but with different text and images)
• About Us (I think that this page can be relatively simple and generic)
• Contact (I think that this page can be very simple and generic)
Nice to have
• An ability to start out basic and quicikly establish a website presence and then build in additional drop downs and pages over time.
Should not have
• It does not need a photo gallery page;
• It does not need a major amount of space dedicated to social media and blogs etc as this is not currently particularly active area for us

```html
<!DOCTYPE html>
<html lang="en">
<head>
<meta charset="utf-8">
<title>Kelvale Ecoservices</title>
<link href="https://fonts.googleapis.com/css2?family=Arimo:wght@400;700&display=swap" rel="stylesheet">
<style>
:root{
  --blue:#33a6d7;
  --green:#9bcb3c;
  --tick:#3a9a3a;
  --ink:#555;
  --ink-soft:#888;
  --heading:#6e6e6e;
  --line:#e3e3e3;
  --footer-bg:#f5f3f3;
  --white:#fff;
  --brand:#6b4a22;
}
*{box-sizing:border-box;margin:0;padding:0}
html,body{width:1200px;height:1105px;overflow:hidden}
body{position:relative;background:var(--white);font-family:"Arimo",Arial,sans-serif;color:var(--ink)}
a{color:inherit;text-decoration:none}
.abs{position:absolute}

/* header */
.site-header{position:absolute;left:0;top:0;width:1200px;height:67px;border-bottom:1px solid var(--line)}
.brand{position:absolute;left:258px;top:18px;display:flex;align-items:center;gap:10px}
.brand-dot{width:26px;height:26px;border-radius:50%;background:var(--green)}
.brand-name{font-size:25px;color:var(--brand);font-weight:400}
.main-nav{position:absolute;right:238px;top:28px;display:flex;font-size:10px;font-weight:700;color:#555}
.main-nav a{padding:0 14px;border-left:1px solid var(--line);line-height:14px}
.main-nav a:first-child{border-left:none}
.main-nav .active{color:var(--blue)}
.caret{font-size:7px;font-weight:400}

/* hero */
.hero{position:absolute;left:0;top:80px;width:1200px;height:266px;background:var(--green);color:var(--white)}
.hero-title{position:absolute;left:258px;top:57px;width:200px;font-size:15px;font-weight:700;line-height:18px}
.hero-text{position:absolute;left:524px;top:55px;width:440px;font-size:8.6px;line-height:14px}
.hero-text p{margin-bottom:14px}

/* feature cards */
.card{position:absolute;top:388px;width:160px;text-align:center}
.card-photo{height:98px;padding:5px;border:1px solid #eee;background:var(--white)}
.card.is-active .card-photo{border:5px solid var(--blue);padding:1px}
.card-photo div{width:100%;height:100%}
.card-title{margin-top:19px;font-size:11.5px;color:#444}
.card.is-active .card-title{color:var(--blue)}
.card-text{margin-top:7px;font-size:8px;line-height:11px;color:var(--ink-soft)}
.divider{position:absolute;left:0;top:589px;width:1200px;height:1px;background:var(--line)}

/* services + about */
.section-title{font-size:15px;font-weight:700;color:var(--heading)}
.body-text{font-size:8.2px;line-height:11.5px;color:var(--ink)}
.services{position:absolute;left:258px;top:625px;width:220px}
.services .body-text{margin-top:15px}
.service-list{list-style:none;margin-top:23px}
.service-list li{display:flex;align-items:center;gap:9px;height:21px;font-size:8.2px;color:var(--ink)}
.about{position:absolute;left:524px;top:625px;width:440px}
.about>.body-text{margin-top:15px}
.about-photo{position:absolute;left:0;top:68px;width:201px;height:114px;background:radial-gradient(circle at 50% 45%,#bfe9ee,#3aa5b5 60%,#1e6f82)}
.about-side{position:absolute;left:224px;top:68px;width:216px}
.about-side p{margin-bottom:11px;line-height:13.5px}

/* footer */
.site-footer{position:absolute;left:0;top:881px;width:1200px;height:178px;background:var(--footer-bg)}
.footer-brand{position:absolute;left:258px;top:38px;display:flex;align-items:center;gap:9px}
.footer-brand .brand-dot{background:#999;width:22px;height:22px}
.footer-brand .brand-name{color:#777;font-size:21px}
.footer-col{position:absolute;top:46px}
.footer-col h4{font-size:8.6px;font-weight:700;color:#666;margin-bottom:17px;letter-spacing:.2px}
.footer-col .body-text{color:var(--ink-soft);line-height:13px}
.office{left:525px}
.office .gap{height:12px}
.related{left:683px}
.related ul{list-style:none}
.related li{font-size:8.2px;color:var(--ink-soft);height:17.5px;display:flex;gap:9px}
.related li .chev{color:#aaa}
.related li.active a{color:var(--blue);text-decoration:underline}
.follow{left:877px}
.social{display:flex;gap:10px}
.social span{width:22px;height:22px;border-radius:50%;background:#8a8a8a}

.bottom-bar{position:absolute;left:0;top:1059px;width:1200px;height:46px}
.copyright{position:absolute;left:258px;top:20px;font-size:8px;color:var(--ink-soft)}
.bottom-nav{position:absolute;right:238px;top:20px;font-size:8px;color:var(--ink-soft)}
.bottom-nav a{padding:0 3px}
.bottom-nav .active{color:var(--blue)}
</style>
</head>
<body>

<header class="site-header">
  <a class="brand" href="#"><span class="brand-dot"></span><span class="brand-name">Kelvale Ecoservices</span></a>
  <nav class="main-nav">
    <a class="active" href="#">Home</a>
    <a href="#">Services <span class="caret">&#8964;</span></a>
    <a href="#">About Us</a>
    <a href="#">Contact</a>
  </nav>
</header>

<section class="hero">
  <h1 class="hero-title">Environmental Planning &amp; Management</h1>
  <div class="hero-text">
    <p>Lorem Ipsum is simply dummy text of the printing and typesetting industry. Lorem Ipsum has been the industry's standard dummy text ever since the 1500s, when an unknown printer took a galley of type and scrambled it to make a type specimen book. It has survived not only five centuries, but also the leap into electronic typesetting, remaining essentially unchanged. It was popularised in the 1960s with the release of Letraset sheets containing Lorem Ipsum passages, and more recently with desktop publishing software like Aldus PageMaker including versions of Lorem Ipsum.</p>
    <p>Lorem ipsum dolor sit amet, consectetur adipiscing elit, sed do eiusmod tempor incididunt ut labore et dolore magna aliqua. Ut enim ad minim veniam, quis nostrud exercitation ullamco laboris nisi ut aliquip ex ea commodo consequat.</p>
    <p>Duis aute irure dolor in reprehenderit in voluptate velit esse cillum dolore eu fugiat nulla pariatur. Excepteur sint occaecat cupidatat non proident, sunt in culpa qui officia deserunt mollit anim id est laborum.</p>
  </div>
</section>

<div class="card is-active" style="left:258px">
  <div class="card-photo"><div role="img" aria-label="Photo of a red native flower among green leaves" style="background:linear-gradient(135deg,#5f7a3a,#b5473a 55%,#4a6a2e)"></div></div>
  <h3 class="card-title">Lorem ipsum dolor sit amet</h3>
  <p class="card-text">Lorem ipsum dolor sit amet, consectetur adipiscing elit, sed do eiusmod</p>
</div>
<div class="card" style="left:439px">
  <div class="card-photo"><div role="img" aria-label="Photo of orange and purple native seed pods" style="background:linear-gradient(135deg,#6d8a4a,#e98a2a 50%,#6a2f52)"></div></div>
  <h3 class="card-title">Lorem ipsum dolor sit amet</h3>
  <p class="card-text">Lorem ipsum dolor sit amet, consectetur adipiscing elit, sed do eiusmod</p>
</div>
<div class="card" style="left:621px">
  <div class="card-photo"><div role="img" aria-label="Photo of a red native flower among green leaves" style="background:linear-gradient(135deg,#5f7a3a,#b5473a 55%,#4a6a2e)"></div></div>
  <h3 class="card-title">Lorem ipsum dolor sit amet</h3>
  <p class="card-text">Lorem ipsum dolor sit amet, consectetur adipiscing elit, sed do eiusmod</p>
</div>
<div class="card" style="left:802px">
  <div class="card-photo"><div role="img" aria-label="Photo of orange and purple native seed pods" style="background:linear-gradient(135deg,#6d8a4a,#e98a2a 50%,#6a2f52)"></div></div>
  <h3 class="card-title">Lorem ipsum dolor sit amet</h3>
  <p class="card-text">Lorem ipsum dolor sit amet, consectetur adipiscing elit, sed do eiusmod</p>
</div>

<div class="divider"></div>

<section class="services">
  <h2 class="section-title">Services</h2>
  <p class="body-text">Lorem ipsum dolor sit amet, consectetur adipiscing elit, sed do eiusmod tempor incididunt ut labore et dolore magna aliqua.</p>
  <ul class="service-list">
    <li><svg width="9" height="8" viewBox="0 0 9 8"><path d="M1 4.2 3.4 6.5 8 1.3" fill="none" stroke="var(--tick)" stroke-width="2"/></svg>Baseline flora and vegetation surveys</li>
    <li><svg width="9" height="8" viewBox="0 0 9 8"><path d="M1 4.2 3.4 6.5 8 1.3" fill="none" stroke="var(--tick)" stroke-width="2"/></svg>Vegetation association mapping</li>
    <li><svg width="9" height="8" viewBox="0 0 9 8"><path d="M1 4.2 3.4 6.5 8 1.3" fill="none" stroke="var(--tick)" stroke-width="2"/></svg>Targeted significant flora and weed surveys</li>
    <li><svg width="9" height="8" viewBox="0 0 9 8"><path d="M1 4.2 3.4 6.5 8 1.3" fill="none" stroke="var(--tick)" stroke-width="2"/></svg>Ethno botanical surveys</li>
    <li><svg width="9" height="8" viewBox="0 0 9 8"><path d="M1 4.2 3.4 6.5 8 1.3" fill="none" stroke="var(--tick)" stroke-width="2"/></svg>Environmental impact assessment</li>
    <li><svg width="9" height="8" viewBox="0 0 9 8"><path d="M1 4.2 3.4 6.5 8 1.3" fill="none" stroke="var(--tick)" stroke-width="2"/></svg>Environmental planning, management and monitoring</li>
    <li><svg width="9" height="8" viewBox="0 0 9 8"><path d="M1 4.2 3.4 6.5 8 1.3" fill="none" stroke="var(--tick)" stroke-width="2"/></svg>Rehabilitation and revegetation planning and implementation.</li>
  </ul>
</section>

<section class="about">
  <h2 class="section-title">About Us</h2>
  <p class="body-text">Lorem ipsum dolor sit amet, consectetur adipiscing elit, sed do eiusmod tempor incididunt ut labore et dolore magna aliqua. Ut enim ad minim veniam, quis nostrud exercitation ullamco laboris nisi ut aliquip ex ea commodo consequat.</p>
  <div class="about-photo" role="img" aria-label="Image of a small tree growing inside a light bulb on a teal background"></div>
  <div class="about-side body-text">
    <p>Lorem Ipsum is simply dummy text of the printing and typesetting industry. Lorem Ipsum has been the industry's standard dummy text ever since the 1500s, when an unknown printer took a galley of type and scrambled it to make a type specimen book. It has survived not only</p>
    <p>Lorem Ipsum is simply dummy text of the printing and typesetting industry. Lorem Ipsum has been the industry's standard dummy text ever since</p>
  </div>
</section>

<footer class="site-footer">
  <div class="footer-brand"><span class="brand-dot"></span><span class="brand-name">Kelvale Ecoservices</span></div>
  <div class="footer-col office">
    <h4>OFFICE LOCATION</h4>
    <p class="body-text">123, Street Name, City Name<br>Country Name - 12345</p>
    <div class="gap"></div>
    <p class="body-text">Phone: 01 1234 1234<br>Fax: 01 1234 1234<br>email: info@example.com</p>
  </div>
  <div class="footer-col related">
    <h4>RELATED LINKS</h4>
    <ul>
      <li><span class="chev">&gt;</span><a href="#">Duis aute irure dolor in reprehenderit</a></li>
      <li class="active"><span class="chev">&gt;</span><a href="#">Voluptate velit esse cillum dolore</a></li>
      <li><span class="chev">&gt;</span><a href="#">Excepteur sint occaecat cupidatat</a></li>
      <li><span class="chev">&gt;</span><a href="#">Officia deserunt mollit anim id est laborum</a></li>
    </ul>
  </div>
  <div class="footer-col follow">
    <h4>FOLLOW US</h4>
    <div class="social"><span></span><span></span><span></span></div>
  </div>
</footer>

<div class="bottom-bar">
  <p class="copyright">© Copyright 2015. Kelvale Ecoservices. All Right Reserved</p>
  <nav class="bottom-nav"><a class="active" href="#">Home</a> | <a href="#">About Us</a> | <a href="#">Contact Us</a> | <a href="#">Privacy Policy</a> | <a href="#">Terms of Uses</a></nav>
</div>

</body>
</html>
```